A ebook cover to reinvent the imagery of vegetable companion gardening

We needs a ebook design with illustrates minimal as well as clear and concise relevance to vegetable companion gardening . we will add a mock up design and other existing designs to help you gauge and create the sort of illustration fit for our aims.
Book Title: Harvest Patch Basics – Vegetable Partner Sowing
Subtitle: Partner Handbook For Raising Crops Through Simple, Natural & Lasting Plot Methods
(Perfect For Beginners)
Author: Tall Meadow
Size: 5.5 x 8.5

```html
<!DOCTYPE html>
<html lang="en">
<head>
<meta charset="utf-8">
<title>Harvest Patch Basics – Vegetable Partner Sowing</title>
<link rel="stylesheet" href="https://fonts.googleapis.com/css2?family=Oswald:wght@700&family=Roboto:wght@900&family=Open+Sans:wght@700&family=Dancing+Script:wght@700&display=swap">
<style>
  :root {
    --backdrop: #eceae6;
    --paper: #ffffff;
    --tan: #e3c27d;
    --tan-light: #ecd59c;
    --leaf: #8dc063;
    --leaf-light: #a9d083;
    --title-green: #6cb43f;
    --crimson: #c8174f;
    --rule-green: #7cba4a;
  }
  * { margin: 0; padding: 0; box-sizing: border-box; }
  html, body {
    width: 1200px;
    height: 1000px;
    overflow: hidden;
    background: var(--backdrop);
  }
  .cover {
    position: absolute;
    left: 310px;
    top: 52px;
    width: 580px;
    height: 896px;
    background: var(--paper);
    overflow: hidden;
    box-shadow: 0 6px 24px rgba(0,0,0,0.18);
  }
  .cover-bands {
    position: absolute;
    inset: 0;
  }
  .title {
    position: absolute;
    right: 42px;
    top: 40px;
    text-align: right;
    font-family: "Oswald", sans-serif;
    font-weight: 700;
    font-size: 66px;
    line-height: 76px;
    text-transform: uppercase;
  }
  .title-top { color: var(--title-green); display: block; }
  .title-bottom { color: var(--crimson); display: block; }
  .series-line {
    position: absolute;
    right: 42px;
    top: 210px;
    font-family: "Roboto", sans-serif;
    font-weight: 900;
    font-size: 19px;
    color: var(--crimson);
    text-transform: uppercase;
    letter-spacing: 0.2px;
  }
  .produce-photo {
    position: absolute;
    left: 0;
    top: 272px;
    width: 485px;
    height: 303px;
    background:
      radial-gradient(circle at 20% 70%, #d23a2a 0 14%, transparent 15%),
      radial-gradient(circle at 55% 55%, #e9a23b 0 13%, transparent 14%),
      radial-gradient(circle at 82% 68%, #8cc43f 0 15%, transparent 16%),
      radial-gradient(circle at 65% 25%, #e8503f 0 11%, transparent 12%),
      radial-gradient(circle at 35% 15%, #f3d23c 0 12%, transparent 13%),
      linear-gradient(120deg, #9bbd3a 0%, #f0c544 30%, #e05a3a 55%, #b7cf4a 80%, #d9374a 100%);
  }
  .subtitle {
    position: absolute;
    left: 30px;
    right: 30px;
    top: 646px;
    text-align: center;
    font-family: "Open Sans", sans-serif;
    font-weight: 700;
    font-size: 14.5px;
    line-height: 19px;
    color: var(--crimson);
  }
  .audience {
    position: absolute;
    left: 0;
    right: 0;
    top: 722px;
    text-align: center;
    font-family: "Dancing Script", cursive;
    font-weight: 700;
    font-size: 27px;
    color: var(--title-green);
  }
  .author-rule {
    position: absolute;
    left: 82px;
    top: 785px;
    width: 412px;
    height: 3px;
    background: var(--rule-green);
  }
  .author {
    position: absolute;
    left: 0;
    right: 0;
    top: 804px;
    text-align: center;
    font-family: "Open Sans", sans-serif;
    font-weight: 700;
    font-size: 25px;
    color: var(--crimson);
  }
</style>
</head>
<body>
  <main class="cover">
    <svg class="cover-bands" width="580" height="896" viewBox="0 0 580 896" aria-hidden="true">
      <defs>
        <linearGradient id="tanFade" x1="0" y1="0" x2="1" y2="0">
          <stop offset="0" stop-color="var(--tan)"/>
          <stop offset="1" stop-color="var(--tan-light)"/>
        </linearGradient>
        <linearGradient id="leafFade" x1="0" y1="0" x2="1" y2="0">
          <stop offset="0" stop-color="var(--leaf-light)"/>
          <stop offset="1" stop-color="var(--leaf)"/>
        </linearGradient>
      </defs>
      <polygon class="band-tan" points="0,0 184,0 0,896" fill="url(#tanFade)"/>
      <polygon class="band-leaf" points="533,0 580,0 580,896 402,896" fill="url(#leafFade)"/>
    </svg>

    <h1 class="title">
      <span class="title-top">Harvest Patch</span>
      <span class="title-bottom">Basics</span>
    </h1>
    <p class="series-line">Vegetable Partner Sowing</p>

    <div class="produce-photo" role="img" aria-label="Photo of assorted fresh fruit: bananas, grapes, kiwi, grapefruit, apples, pear, strawberries and berries"></div>

    <p class="subtitle">Partner Handbook For Raising Crops Through Simple,<br>Natural &amp; Lasting Plot Methods</p>
    <p class="audience">[Perfect For Beginners]</p>
    <div class="author-rule"></div>
    <p class="author">Author: Tall Meadow</p>
  </main>
</body>
</html>
```